QOR Infographic Design and Business Card design

We have an infographic but it could use some updating and creativity applied to it. Would like to match it a bit more to our current logo and web design (although it doesn’t have to match per se, thinking of updating it too) http://qor-advisory.example/QOR_Advisory/QOR_Advisory___Your_treasury_pricing_and_fee_negotiation_specialists.html
Can be double sided

Target Market(s)

Companies that make more than $150MM a year

Industry/Entity Type

Business

Contact Information for Business Card

Uploaded the logo and you can also look at the website.

Font styles to use
Sans Serif

Requirements
Must have
• Must look professional. Looking to stick to the same colors in the logo, the logo won’t change. Very open after that
Nice to have
• Front and back on the card

```html
<!DOCTYPE html>
<html lang="en">
<head>
<meta charset="utf-8">
<title>QOR Advisory – Business Card and Infographic</title>
<link href="https://fonts.googleapis.com/css2?family=Open+Sans:wght@400;600;700&family=Oswald:wght@500&display=swap" rel="stylesheet">
<style>
:root{
  --navy:#3d4f61;
  --navy-dark:#33434f;
  --green:#7cb83d;
  --green-head:#8cc43f;
  --paper:#f2f2f2;
  --band:#e4e4e4;
  --text:#3a3a3a;
  --muted:#5a5a5a;
  --stage:#dcdcdc;
  --bar-track:#d6d6d6;
}
*{box-sizing:border-box;margin:0;padding:0}
html,body{width:1200px;height:800px;overflow:hidden}
body{background:var(--stage);font-family:"Open Sans",Arial,sans-serif;color:var(--text);position:relative}
.abs{position:absolute}

/* brand lockup */
.brand{display:flex;align-items:center;gap:6px;font-weight:700;white-space:nowrap}
.brand-dot{border-radius:50%;border:3px solid var(--green);flex:none}

/* business card front */
.card-front{left:105px;top:191px;width:326px;height:191px;background:var(--paper);box-shadow:0 2px 6px rgba(0,0,0,.25);overflow:hidden}
.card-name{left:16px;top:24px;font-size:11px;font-weight:700;color:var(--green);letter-spacing:.2px}
.card-role{left:16px;top:39px;font-size:7.5px;color:var(--text)}
.card-address{left:16px;top:62px;font-size:7.5px;line-height:11.5px}
.card-contacts{left:16px;top:102px;list-style:none;font-size:7.5px}
.card-contacts li{display:flex;align-items:center;gap:4px;height:12.8px}
.card-contacts svg{width:8px;height:8px}
.card-front .brand-stack{right:14px;top:28px;width:150px;flex-direction:column;gap:4px;font-size:12.5px;color:var(--navy)}
.card-front .brand-dot{width:26px;height:26px}
.card-band{left:0;bottom:0;width:326px;height:14px}

/* business card back */
.card-back{left:105px;top:417px;width:326px;height:192px;background:var(--navy);box-shadow:0 2px 6px rgba(0,0,0,.25);display:flex;align-items:center;justify-content:center}
.card-back .brand{font-size:16px;color:#fff;gap:8px}
.card-back .brand-dot{width:34px;height:34px;border-width:4px}

/* infographic */
.sheet{left:529px;top:50px;width:542px;height:700px;background:var(--paper);box-shadow:0 2px 8px rgba(0,0,0,.25);overflow:hidden}
.sec{position:absolute;left:0;width:542px}
.sec-head{top:0;height:156px;background:var(--navy);border-top:4px solid var(--navy-dark)}
.sec-savings{top:156px;height:155px;background:var(--band)}
.sec-process{top:311px;height:196px;background:var(--paper)}
.sec-how{top:507px;height:89px;background:var(--band)}
.sec-expect{top:596px;height:104px;background:var(--paper)}
.divider{border-top:1.5px dotted #9a9a9a}
.sheet .brand{left:22px;top:16px;font-size:13px;color:#fff}
.sheet .brand-dot{width:22px;height:22px}
.heading{font-family:"Oswald","Arial Narrow",sans-serif;font-weight:500;font-size:15px;line-height:18px;text-transform:uppercase;letter-spacing:.1px}
.heading-light{color:#fff}
.heading-green{color:var(--green-head)}
.body{font-size:9.6px;line-height:13px}
.body-light{color:#e2e7ec}
.side-note{font-size:9.6px;line-height:13px;text-align:right;color:var(--text)}
.illus{border-radius:6px}

.service{position:absolute;top:74px;width:60px;text-align:center}
.service-icon{width:39px;height:39px;margin:0 auto;background:var(--navy);border-radius:3px;display:flex;align-items:center;justify-content:center}
.service-icon svg{width:27px;height:27px}
.service-label{font-size:9.6px;line-height:10.5px;margin-top:7px;color:var(--muted)}

.bars{left:18px;top:95px;width:246px;list-style:none}
.bars li{position:relative;height:13px;margin-bottom:10px;background:var(--bar-track);border-radius:7px}
.bar-fill{position:absolute;left:0;top:0;height:13px;background:var(--navy);border-radius:7px;color:#fff;font-size:9.2px;line-height:13px;text-align:right;padding-right:6px;white-space:nowrap}

.checks{list-style:none;left:18px;top:36px;font-size:9.6px}
.checks li{display:flex;align-items:center;gap:5px;height:14px}
.checks svg{width:9px;height:9px;flex:none}
</style>
</head>
<body>

<!-- Business card front -->
<section class="abs card-front" aria-label="Business card front">
  <p class="abs card-name">DANIEL EVERETT</p>
  <p class="abs card-role">Founder / CEO</p>
  <p class="abs card-address">4410 Harbor Point Drive<br>Suite 310<br>Lakeview, FL 32000</p>
  <ul class="abs card-contacts">
    <li><svg viewBox="0 0 10 10"><circle cx="5" cy="5" r="5" fill="#3d4f61"/><rect x="3.3" y="2" width="3.4" height="6" rx=".6" fill="#fff"/></svg>+ 000 000 0000</li>
    <li><svg viewBox="0 0 10 10"><circle cx="5" cy="5" r="5" fill="#3d4f61"/><rect x="2.3" y="3.5" width="5.4" height="3.5" rx=".6" fill="#fff"/></svg>+ 000 000 0000</li>
    <li><svg viewBox="0 0 10 10"><circle cx="5" cy="5" r="5" fill="#3d4f61"/><rect x="2.5" y="3" width="5" height="4" fill="#fff"/></svg>+ 000 000 0000</li>
    <li><svg viewBox="0 0 10 10"><circle cx="5" cy="5" r="5" fill="#3d4f61"/><rect x="2.3" y="3" width="5.4" height="4" fill="#fff"/><path d="M2.3 3l2.7 2 2.7-2" stroke="#3d4f61" stroke-width=".7" fill="none"/></svg>info@qoradvisory.example</li>
    <li><svg viewBox="0 0 10 10"><circle cx="5" cy="5" r="5" fill="#3d4f61"/><circle cx="5" cy="5" r="2.7" stroke="#fff" stroke-width=".8" fill="none"/><path d="M2.3 5h5.4M5 2.3v5.4" stroke="#fff" stroke-width=".6"/></svg>www.qoradvisory.example</li>
  </ul>
  <div class="abs brand brand-stack"><span class="brand-dot"></span>QOR-Advisory.example</div>
  <svg class="abs card-band" viewBox="0 0 326 14" preserveAspectRatio="none">
    <rect width="326" height="14" fill="#3d4f61"/>
    <polygon points="0,0 92,0 84,14 0,14" fill="#7cb83d"/>
    <polygon points="95,0 99,0 91,14 87,14" fill="#ffffff"/>
    <polygon points="164,0 168,0 160,14 156,14" fill="#ffffff"/>
  </svg>
</section>

<!-- Business card back -->
<section class="abs card-back" aria-label="Business card back">
  <div class="brand"><span class="brand-dot"></span>QOR-Advisory.example</div>
</section>

<!-- Infographic -->
<article class="abs sheet" aria-label="Bank savings infographic">

  <section class="sec sec-head">
    <div class="abs brand"><span class="brand-dot"></span>QOR-Advisory.example</div>
    <h1 class="abs heading heading-light" style="left:18px;top:48px;font-size:16px">Are you overpaying your bank?</h1>
    <p class="abs body body-light" style="left:18px;top:72px;width:330px">Clients are faced with two challenges when it comes to their strategic bank relationships. “Where to focus energy for a maximum return and how to negotiate these discounts in order to not disrupt the symbiotic relationship”. You need their credit, products and advisory services, but are you paying too much?</p>
    <div class="abs illus" role="img" aria-label="Illustration of a businessman surrounded by bank card, cash and money bag icons" style="left:374px;top:28px;width:154px;height:122px;background:radial-gradient(circle at 50% 60%,#8a9aab,#4f6275 70%)"></div>
  </section>

  <section class="sec sec-savings">
    <h2 class="abs heading heading-green" style="left:18px;top:18px">Where would your company find bank savings?</h2>
    <p class="abs body" style="left:18px;top:38px;width:270px">There are five key treasury management categories of bank revenue that offer significant opportunity:</p>
    <p class="abs side-note" style="left:396px;top:16px;width:132px">For-profit and non-profit companies with $150 million or more in revenue</p>

    <div class="service" style="left:8px"><div class="service-icon"><svg viewBox="0 0 24 24"><path d="M3 12L12 4l9 8h-3v8h-4v-5h-4v5H6v-8z" fill="#fff"/></svg></div><p class="service-label">Analysis<br>fees</p></div>
    <div class="service" style="left:67px"><div class="service-icon"><svg viewBox="0 0 24 24"><circle cx="7" cy="7" r="3" stroke="#fff" stroke-width="2" fill="none"/><circle cx="17" cy="17" r="3" stroke="#fff" stroke-width="2" fill="none"/><path d="M18 4L6 20" stroke="#fff" stroke-width="2.2"/></svg></div><p class="service-label">Earnings<br>Credit Rate</p></div>
    <div class="service" style="left:126px"><div class="service-icon"><svg viewBox="0 0 24 24"><rect x="3" y="15" width="3" height="6" fill="#fff"/><rect x="8" y="12" width="3" height="9" fill="#fff"/><rect x="13" y="9" width="3" height="12" fill="#fff"/><rect x="18" y="6" width="3" height="15" fill="#fff"/><path d="M3 11l6-4 4 3 7-6" stroke="#fff" stroke-width="1.6" fill="none"/></svg></div><p class="service-label">Investment<br>Rate</p></div>
    <div class="service" style="left:185px"><div class="service-icon"><svg viewBox="0 0 24 24"><rect x="3" y="6" width="18" height="12" rx="1.5" fill="#fff"/><rect x="3" y="9" width="18" height="2.5" fill="#3d4f61"/><rect x="5" y="14" width="6" height="1.5" fill="#3d4f61"/></svg></div><p class="service-label">P-Card<br>Rebates</p></div>
    <div class="service" style="left:244px"><div class="service-icon"><svg viewBox="0 0 24 24"><rect x="5" y="2" width="14" height="20" rx="1.5" fill="#fff"/><rect x="7.5" y="4.5" width="9" height="4" fill="#3d4f61"/><g fill="#3d4f61"><rect x="7.5" y="11" width="2.5" height="2.5"/><rect x="10.8" y="11" width="2.5" height="2.5"/><rect x="14" y="11" width="2.5" height="2.5"/><rect x="7.5" y="14.5" width="2.5" height="2.5"/><rect x="10.8" y="14.5" width="2.5" height="2.5"/><rect x="14" y="14.5" width="2.5" height="2.5"/><rect x="7.5" y="18" width="2.5" height="2"/><rect x="10.8" y="18" width="2.5" height="2"/><rect x="14" y="18" width="2.5" height="2"/></g></svg></div><p class="service-label">Merchant<br>Card</p></div>

    <div class="abs illus" role="img" aria-label="Illustration of a magnifying glass over a bank building" style="left:383px;top:66px;width:144px;height:80px;background:linear-gradient(135deg,#8fa0b1,#d8c9a2)"></div>
  </section>

  <section class="sec sec-process divider">
    <h2 class="abs heading heading-green" style="left:18px;top:16px">Is it a lengthy and involved process?</h2>
    <p class="abs body" style="left:18px;top:38px;width:250px">IT’S REALLY NOT. Anticipate a 2-3 week turnaround for typical project results as demand for your team’s time and resources are minimized by TMA providing profitability reporting and bank correspondence.</p>
    <p class="abs side-note" style="left:380px;top:16px;width:148px;font-size:11px;line-height:14px">98% Success Rate</p>
    <p class="abs side-note" style="left:380px;top:35px;width:148px;font-size:11px;line-height:13px">Client savings range from 15% to 60%</p>
    <ul class="abs bars">
      <li><span class="bar-fill" style="width:246px">Real Estate Investment Trust - $ 1.43MM</span></li>
      <li><span class="bar-fill" style="width:220px">National Healthcare Provider - $1.28MM</span></li>
      <li><span class="bar-fill" style="width:196px">Non-Profit Humanity Group - $1.10MM</span></li>
      <li><span class="bar-fill" style="width:175px">National Restaurant Chain - $1MM</span></li>
    </ul>
    <div class="abs illus" role="img" aria-label="Illustration of an hourglass with coins, a clock, a target and banknotes" style="left:395px;top:72px;width:132px;height:112px;background:linear-gradient(160deg,#9fb3c6,#e7b94a 55%,#6fb26b)"></div>
  </section>

  <section class="sec sec-how divider">
    <h2 class="abs heading heading-green" style="left:20px;top:14px">So how does it work?</h2>
    <p class="abs body" style="left:20px;top:37px;width:280px">ONCE WE RECEIVE YOUR STATEMENTS, we examine all areas for profitability and relationship value, analyzing both your quantitative and qualitative data.</p>
    <div class="abs illus" role="img" aria-label="Illustration of interlocking gears" style="left:304px;top:12px;width:64px;height:66px;background:radial-gradient(circle,#6d7f91,#3d4f61 70%)"></div>
    <p class="abs side-note" style="left:378px;top:13px;width:150px">There are dozens of categories of influence that dictate pricing, rates and your overall discount</p>
  </section>

  <section class="sec sec-expect divider">
    <h2 class="abs heading heading-green" style="left:18px;top:14px">What can you expect?</h2>
    <ul class="abs checks">
      <li><svg viewBox="0 0 10 10"><circle cx="5" cy="5" r="5" fill="#3d4f61"/><path d="M2.7 5.2l1.6 1.6 3-3.2" stroke="#fff" stroke-width="1.2" fill="none"/></svg>Never require you to switch providers for savings</li>
      <li><svg viewBox="0 0 10 10"><circle cx="5" cy="5" r="5" fill="#3d4f61"/><path d="M2.7 5.2l1.6 1.6 3-3.2" stroke="#fff" stroke-width="1.2" fill="none"/></svg>Proactively provide win-win solutions for your banks</li>
      <li><svg viewBox="0 0 10 10"><circle cx="5" cy="5" r="5" fill="#3d4f61"/><path d="M2.7 5.2l1.6 1.6 3-3.2" stroke="#fff" stroke-width="1.2" fill="none"/></svg>Appreciate the advisory relationship you have with your bank</li>
      <li><svg viewBox="0 0 10 10"><circle cx="5" cy="5" r="5" fill="#3d4f61"/><path d="M2.7 5.2l1.6 1.6 3-3.2" stroke="#fff" stroke-width="1.2" fill="none"/></svg>Client retains 100% control of the timing, process and communications</li>
    </ul>
    <div class="abs illus" role="img" aria-label="Illustration of a cheering businessman with banknotes falling around him" style="left:395px;top:-8px;width:132px;height:112px;background:linear-gradient(180deg,#efe6bf,#c9d9a8 60%,#3d4f61)"></div>
  </section>

</article>
</body>
</html>
```